Modern luxury trendy cosmetics label

Looking for a cosmetics packaging label design. We are looking for a professionel, modern and luxury look like Lorena Vasquel, Meadowkin Apothecary, Marigold Tessin, Gavin Albert Pruke, Zuna, Orvik + Dalle, Velumi, Sleepy Walrus, the plainfold, lumiere de sable.Name of product: Nordic Tulip Mask - Needle-Free Contour Ritual Ingredients that have scientific proof of anti aging: Cherry blossom extact, collegen, hyaluronic acid, coconut oil. Color of product itself: Pastel pink. Smell: Cherry blossom. Colors of label: simple and black and white or some subtle colors.

Target Market(s)

Women, luxury market, modern women, young and old women

Industry/Entity Type

Cosmetics

Font styles to use
Sans Serif

Colors

Designer to choose colors to be used in the design.

Requirements
Must have
• A modern look, professional, cosmetics, beauty, professional market, original

```html
<!DOCTYPE html>
<html lang="en">
<head>
<meta charset="utf-8">
<title>Nordic Tulip Mask – Label</title>
<link rel="stylesheet" href="https://fonts.googleapis.com/css2?family=Josefin+Sans:wght@300;600&family=Quicksand:wght@400&family=Satisfy&display=swap">
<style>
  :root {
    --blush: #f8dde3;
    --blush-deep: #efc3cd;
    --white: #ffffff;
    --ink: #1d1a1a;
    --grey: #7a7a7a;
    --plum: #5b1a44;
    --petal: #eea3b1;
  }
  * { margin: 0; padding: 0; box-sizing: border-box; }
  html, body { width: 1200px; height: 1000px; overflow: hidden; background: var(--white); }
  .canvas { position: relative; width: 1200px; height: 1000px; overflow: hidden; background: var(--white); }

  .label-band { position: absolute; left: 0; top: 0; width: 1200px; height: 592px; }
  .band-top { position: absolute; left: 0; top: 0; width: 100%; height: 18px; background: var(--blush); }
  .band-main { position: absolute; left: 0; top: 26px; width: 100%; height: 538px; background: var(--blush); }
  .band-bottom { position: absolute; left: 0; top: 572px; width: 100%; height: 18px; background: var(--blush); }
  .side-pattern { position: absolute; top: 26px; height: 538px; width: 180px;
    background: linear-gradient(180deg, var(--blush) 0%, #f3d0d8 50%, var(--blush) 100%); }
  .side-pattern.left { left: 0; }
  .side-pattern.right { right: 0; }

  .label-disc { position: absolute; left: 140px; top: -330px; width: 920px; height: 920px;
    border-radius: 50%; background: var(--white); }

  .label-text { position: absolute; left: 0; top: 0; width: 1200px; text-align: center; }
  .therapy { position: absolute; top: 44px; width: 100%; font-family: "Josefin Sans", sans-serif;
    font-weight: 300; font-size: 29px; letter-spacing: 1px; word-spacing: 8px; color: var(--ink); }
  .ingredients { position: absolute; top: 82px; width: 100%; font-family: "Josefin Sans", sans-serif;
    font-weight: 300; font-size: 18px; word-spacing: 5px; color: var(--ink); }
  .brand { position: absolute; top: 152px; width: 100%; font-family: "Quicksand", sans-serif;
    font-size: 58px; color: var(--grey); letter-spacing: 1px; }
  .product-name { position: absolute; top: 280px; width: 100%; font-family: "Josefin Sans", sans-serif;
    font-weight: 300; font-size: 64px; color: var(--ink); letter-spacing: -1px; }
  .product-name .cap { font-weight: 600; font-size: 84px; }

  .scent { position: absolute; top: 438px; width: 100%; display: flex; justify-content: center;
    align-items: center; gap: 22px; font-family: "Satisfy", cursive; font-size: 64px; color: var(--plum); }
  .blossom-mark { width: 92px; height: 92px; border-radius: 50%; background: radial-gradient(circle, #e88a9c 0%, var(--petal) 60%, #f3bcc7 100%); }

  .jar { position: absolute; top: 618px; width: 396px; height: 366px; border-radius: 40px 40px 60px 60px;
    background: linear-gradient(180deg, #f4f4f4 0%, #ffffff 28%, #e9c6cd 40%, #f6e3e7 70%, #e5e5e5 100%); }
  .jar.left { left: 180px; }
  .jar.right { left: 634px; }
</style>
</head>
<body>
<main class="canvas">
  <section class="label-band">
    <div class="band-top"></div>
    <div class="band-main"></div>
    <div class="band-bottom"></div>
    <div class="side-pattern left" role="img" aria-label="Line-drawn cherry blossom pattern on pink"></div>
    <div class="side-pattern right" role="img" aria-label="Line-drawn cherry blossom pattern on pink"></div>
    <div class="label-disc"></div>

    <div class="label-text">
      <p class="therapy">Needle-Free Contour Ritual</p>
      <p class="ingredients">Cherry blossom extact, collegen, hyaluronic acid, coconut oil</p>
      <p class="brand">velora</p>
      <h1 class="product-name"><span class="cap">N</span>ordic <span class="cap">T</span>ulip <span class="cap">M</span>ask</h1>
      <div class="scent">
        <span>Cherry</span>
        <div class="blossom-mark" role="img" aria-label="Pink cherry blossom flower illustration"></div>
        <span>Blossom</span>
      </div>
    </div>
  </section>

  <div class="jar left" role="img" aria-label="White mask jar wearing the pink and white label"></div>
  <div class="jar right" role="img" aria-label="White mask jar wearing the pink and white label"></div>
</main>
</body>
</html>
```